Pediatric Vision Care: Myopia Control Brochure

We are a pediatric eye care practice (ophthalmology and optometry). One of our services we offer for children is myopia control, which are strategies for slowing or stopping the progression of nearsightedness. This is a service we need to sell to parents because most insurance won't pay for it. There are different options we offer that can work well for kids in different situations: glasses with Corvane lenses, atropine eye drops, and/or special contact lenses. We need a brochure we can distribute to parents to let them know about this service that would encourage them to buy it for children who need it. Attached is our initial draft brochure created by our staff that provides text that we want to keep. The images and layout can change. We probably need at least one or two photos of kids on the brochure, because this is only something that works for children who are still growing, and the target audience is parents of 4-8 year old children.

Target Market(s)

Parents of 4-8 year old children

Font styles to use
Sans Serif

Requirements
Must have
• I'm uploading our company logo that should be included somewhere on the brochure. You can include contact information (web address, phone number) for our practice that is found on our website: http://www.brookhollowkidsvision.com/
Should not have
• This should not look childish. We need the impression to be friendly but professional, medical, expert.

```html
<!DOCTYPE html>
<html lang="en">
<head>
<meta charset="utf-8">
<title>Brookhollow Kids Vision – Myopia Control Brochure</title>
<link href="https://fonts.googleapis.com/css2?family=Barlow:wght@400;500;600;700&display=swap" rel="stylesheet">
<style>
:root{
  --stage:#4a4a4a;
  --ink:#232323;
  --purple:#6a72b8;
  --purple-deep:#5b63b0;
  --green:#8cc43c;
  --green-deep:#6fae25;
  --orange:#f08a1c;
  --yellow:#f6c21b;
  --white:#ffffff;
  --navy:#2d3a6b;
}
*{margin:0;padding:0;box-sizing:border-box}
html,body{width:1200px;height:2483px;overflow:hidden}
body{background:var(--stage);font-family:'Barlow',sans-serif;color:var(--ink);position:relative}
.spread{position:absolute;left:30px;width:1140px;height:881px;background:var(--white);overflow:hidden;box-shadow:0 6px 24px rgba(0,0,0,.35)}
.spread--outside{top:330px}
.spread--inside{top:1271px}
.spread svg.backdrop{position:absolute;left:0;top:0;width:1140px;height:881px}
.block{position:absolute}
.section-title{font-weight:700;font-size:24px;color:var(--orange)}
.body-copy{font-size:16.5px;line-height:21px}
.body-copy p+p{margin-top:21px}
.appointment-title{font-weight:700;font-size:27px;line-height:28px;color:var(--white);text-align:right}
.contact-line{font-size:17px;color:var(--white);line-height:24.5px}
.contact-line b{font-weight:600;color:#fff7c2}
.address-box{background:var(--white);border:3px solid var(--purple);border-radius:10px;padding:10px 22px;font-size:16.5px;line-height:19px}
.address-box .label{color:var(--orange)}
.email-line{font-size:16.5px;color:var(--white)}
.email-line b{font-weight:500;color:#fff7c2}
.url-line{font-size:16.5px;letter-spacing:1.6px;color:var(--white);font-weight:500}
.brand{display:flex;align-items:center;gap:10px;font-weight:500;color:var(--navy);line-height:1.05}
.brand__dot{width:22px;height:22px;border-radius:50%;background:var(--green)}
.headline{font-weight:700;font-size:42px;line-height:43px}
.headline .purple{color:var(--purple-deep)}
.headline .green{color:var(--green-deep)}
.rule{height:4px;background:var(--orange)}
.cover-copy{font-size:16px;line-height:19px}
.cover-url{font-size:16.5px;color:var(--white)}
.band-copy{font-size:17px;line-height:21px;color:var(--white)}
.band-copy p+p{margin-top:21px}
.option-title{font-weight:700;font-size:24px;line-height:27px}
.option-copy{font-size:16.5px;line-height:24px}
.option-copy p+p{margin-top:24px}
.photo-tag{font-size:19px;color:var(--white)}
</style>
</head>
<body>

<!-- OUTSIDE SPREAD -->
<section class="spread spread--outside">
  <svg class="backdrop" viewBox="0 0 1140 881">
    <defs>
      <linearGradient id="coverBg" x1="0" y1="0" x2="0" y2="1">
        <stop offset="0" stop-color="#fffef8"/>
        <stop offset=".55" stop-color="#fff2c8"/>
        <stop offset="1" stop-color="#fbd98a"/>
      </linearGradient>
      <linearGradient id="examPhoto" x1="0" y1="0" x2="1" y2="1">
        <stop offset="0" stop-color="#6b4a3c"/>
        <stop offset=".5" stop-color="#b69aa8"/>
        <stop offset="1" stop-color="#3b3a3e"/>
      </linearGradient>
      <linearGradient id="doctorPhoto" x1="0" y1="0" x2="1" y2="1">
        <stop offset="0" stop-color="#e9e4da"/>
        <stop offset=".5" stop-color="#f5f3ef"/>
        <stop offset="1" stop-color="#9a9690"/>
      </linearGradient>
      <linearGradient id="kidPhoto" x1="0" y1="0" x2="0" y2="1">
        <stop offset="0" stop-color="#c79a7a"/>
        <stop offset=".5" stop-color="#7f9bb4"/>
        <stop offset="1" stop-color="#e8d3a8"/>
      </linearGradient>
      <radialGradient id="eyeDiagram">
        <stop offset="0" stop-color="#e05a3a"/>
        <stop offset=".6" stop-color="#f2b7a0"/>
        <stop offset="1" stop-color="#ffffff"/>
      </radialGradient>
    </defs>

    <rect x="0" y="0" width="384" height="881" fill="var(--white)"/>
    <rect x="769" y="0" width="371" height="881" fill="url(#coverBg)"/>

    <path role="img" aria-label="Photo of a doctor fitting a trial frame on a young girl in an exam room" d="M384 0 H769 V500 H384 Z" fill="url(#doctorPhoto)"/>
    <path role="img" aria-label="Photo of a clinician placing a phoropter in front of a smiling girl" d="M0 605 C200 540 300 488 384 458 L384 881 L0 881 Z" fill="url(#examPhoto)"/>

    <path d="M384 470 C520 420 650 372 769 338 L769 881 L384 881 Z" fill="var(--green)"/>
    <path d="M0 590 C200 525 300 475 384 445 C520 395 650 350 769 315" fill="none" stroke="var(--yellow)" stroke-width="9"/>
    <rect x="728" y="410" width="4" height="0" fill="none"/>
    <rect x="715" y="410" width="54" height="4" fill="var(--yellow)"/>

    <path d="M384 806 C500 738 650 742 769 798 L769 881 L384 881 Z" fill="var(--white)"/>
    <path d="M384 792 C500 722 640 728 769 782" fill="none" stroke="var(--orange)" stroke-width="14"/>
    <path d="M384 776 C500 706 640 712 769 766" fill="none" stroke="var(--yellow)" stroke-width="8"/>

    <path role="img" aria-label="Photo of a boy in glasses covering one eye with his hand" d="M985 420 H1140 V800 H985 Z" fill="url(#kidPhoto)"/>

    <path d="M769 752 C880 700 1000 718 1140 688 L1140 712 C1000 742 880 726 769 776 Z" fill="var(--green)"/>
    <path d="M769 770 C880 722 1000 740 1140 706 L1140 881 L769 881 Z" fill="var(--purple)"/>

    <circle cx="906" cy="713" r="95" fill="var(--white)" stroke="var(--yellow)" stroke-width="6"/>
    <circle role="img" aria-label="Diagram comparing a myopic eye with a normal eye" cx="920" cy="713" r="62" fill="url(#eyeDiagram)"/>
  </svg>

  <h2 class="block section-title" style="left:30px;top:32px">Environmental Options:</h2>
  <div class="block body-copy" style="left:30px;top:82px;width:330px">
    <p>All myopic children can benefit from these lifestyle changes. It is important to get your child outdoors consistently. There is strong evidence that children who spend at least 2 hours a day outdoors are less likely to become myopic, and their myopia progresses slower than children who are outdoors less. Some studies show that increasing outdoor time by as few as 45 minutes a day is beneficial in reducing progression.</p>
    <p>There is some evidence that consistent use of screens, particularly held very close to the face, can worsen nearsightedness. We recommend limiting nonacademic screen time and near work, and encourage your child to use the 20-20-20 rule. Every 20 minutes take a 20 second break to look at least 20 feet away.</p>
  </div>

  <h2 class="block appointment-title" style="right:395px;top:366px">Make An<br>Appointment</h2>
  <div class="block" style="left:443px;top:442px">
    <div class="contact-line">Voice Call: <b>(555) 214-0190</b></div>
    <div class="contact-line">Text Message: <b>(555) 214-3377</b></div>
    <div class="contact-line">Fax: <b>(555) 214-4590</b></div>
  </div>
  <div class="block address-box" style="left:443px;top:529px;width:268px">
    <div class="label">Address:</div>
    Brookhollow Kids Vision<br>2180 Larkspur Avenue<br>Fairhaven, VA 23000
  </div>
  <div class="block email-line" style="left:443px;top:663px">Email: <b>info@brookhollowkidsvision.com</b></div>
  <div class="block url-line" style="left:438px;top:696px">www.brookhollowkidsvision.com</div>

  <div class="block brand" style="left:448px;top:816px;font-size:22px">
    <span class="brand__dot"></span><span>Brookhollow Kids Vision</span>
  </div>

  <div class="block brand" style="left:800px;top:70px;font-size:27px;width:320px">
    <span class="brand__dot" style="width:28px;height:28px"></span><span>Brookhollow<br>Kids Vision</span>
  </div>
  <h1 class="block headline" style="left:800px;top:180px">
    <span class="purple">Every Child<br>Deserves To</span><br>
    <span class="green">See The World<br>Clearly</span>
  </h1>
  <div class="block rule" style="left:800px;top:375px;width:125px"></div>
  <p class="block cover-copy" style="left:800px;top:405px;width:170px">Our doctors draw on decades of experience, state-of-the-art technology, and cutting edge research to help children achieve their best possible vision.</p>
  <div class="block cover-url" style="left:835px;top:828px">www.brookhollowkidsvision.com</div>
</section>

<!-- INSIDE SPREAD -->
<section class="spread spread--inside">
  <svg class="backdrop" viewBox="0 0 1140 881">
    <defs>
      <linearGradient id="colPeach" x1="0" y1="0" x2="0" y2="1"><stop offset="0" stop-color="#fdd7b4"/><stop offset=".75" stop-color="#ffffff"/></linearGradient>
      <linearGradient id="colYellow" x1="0" y1="0" x2="0" y2="1"><stop offset="0" stop-color="#fde6a2"/><stop offset=".75" stop-color="#ffffff"/></linearGradient>
      <linearGradient id="colGreen" x1="0" y1="0" x2="0" y2="1"><stop offset="0" stop-color="#d3e6ad"/><stop offset=".75" stop-color="#ffffff"/></linearGradient>
      <linearGradient id="band" x1="0" y1="0" x2="1" y2="0"><stop offset="0" stop-color="#6a72b8"/><stop offset="1" stop-color="#7d86c6"/></linearGradient>
      <linearGradient id="glassesPhoto" x1="0" y1="0" x2="1" y2="0">
        <stop offset="0" stop-color="#7d86c6" stop-opacity="0"/>
        <stop offset=".35" stop-color="#d9b9a0"/>
        <stop offset="1" stop-color="#f1ece6"/>
      </linearGradient>
      <linearGradient id="framesPhoto" x1="0" y1="0" x2="1" y2="1"><stop offset="0" stop-color="#e8e2dc"/><stop offset="1" stop-color="#8a5a44"/></linearGradient>
      <linearGradient id="lensPhoto" x1="0" y1="0" x2="1" y2="1"><stop offset="0" stop-color="#2f7c86"/><stop offset="1" stop-color="#163d48"/></linearGradient>
      <linearGradient id="dropPhoto" x1="0" y1="0" x2="1" y2="1"><stop offset="0" stop-color="#8fb1c4"/><stop offset="1" stop-color="#2b4656"/></linearGradient>
      <linearGradient id="contactPhoto" x1="0" y1="0" x2="1" y2="1"><stop offset="0" stop-color="#b34a3c"/><stop offset=".6" stop-color="#4a8fc8"/><stop offset="1" stop-color="#1c1a24"/></linearGradient>
    </defs>

    <rect x="0" y="0" width="380" height="881" fill="url(#colPeach)"/>
    <rect x="380" y="0" width="380" height="881" fill="url(#colYellow)"/>
    <rect x="760" y="0" width="380" height="881" fill="url(#colGreen)"/>
    <rect x="379" y="309" width="3" height="572" fill="var(--white)"/>
    <rect x="759" y="309" width="3" height="572" fill="var(--white)"/>

    <rect x="0" y="0" width="1140" height="309" fill="url(#band)"/>
    <rect role="img" aria-label="Photo of a red-haired boy holding up a pair of glasses" x="700" y="0" width="440" height="309" fill="url(#glassesPhoto)"/>

    <path d="M640 309 C800 300 960 262 1140 214 L1140 309 Z" fill="var(--white)"/>
    <path d="M620 309 C760 220 900 178 1140 182" fill="none" stroke="var(--orange)" stroke-width="16"/>
    <path d="M800 260 C920 212 1030 208 1140 218" fill="none" stroke="var(--green)" stroke-width="10"/>

    <circle cx="872" cy="229" r="95" fill="var(--white)" stroke="var(--yellow)" stroke-width="6"/>
    <circle role="img" aria-label="Photo of a girl choosing frames from an eyewear display" cx="872" cy="229" r="88" fill="url(#framesPhoto)"/>

    <rect role="img" aria-label="Photo of a spectacle lens with concentric myopia-control rings" x="30" y="660" width="325" height="188" fill="url(#lensPhoto)" stroke="var(--green)" stroke-width="4"/>
    <rect role="img" aria-label="Photo of an eye-drop bottle releasing a single drop" x="416" y="660" width="324" height="188" fill="url(#dropPhoto)" stroke="var(--green)" stroke-width="4"/>
    <rect role="img" aria-label="Photo of a soft contact lens resting on a fingertip" x="793" y="660" width="324" height="188" fill="url(#contactPhoto)" stroke="var(--green)" stroke-width="4"/>
  </svg>

  <h2 class="block section-title" style="left:30px;top:32px;color:var(--yellow)">Myopia Control</h2>
  <div class="block band-copy" style="left:30px;top:74px;width:590px">
    <p>Myopia or nearsightedness causes blurry distance vision. Myopia is caused by the elongation of the eye, and progresses throughout childhood. Myopia is becoming increasingly common. More severe myopia and a higher glasses prescription is associated with a higher risk of eye problems involving the retina in adulthood, such as retinal problems and macular degeneration.</p>
    <p>Myopia control is meant to slow the growth of the eye, keeping the glasses prescription as low as possible and reducing the risk of ocular disease in adulthood. There are several treatment options</p>
  </div>

  <h3 class="block option-title" style="left:30px;top:350px">Lumora Corvane<br>Glasses Lenses</h3>
  <div class="block option-copy" style="left:30px;top:418px;width:330px;line-height:21px">
    <p>FDA market authorized Lumora Corvane glasses lenses have been shown to slow myopia progression by about 50% in children aged 6-12.</p>
    <p style="margin-top:21px">These lenses are a great treatment option because all your child needs to do is wear glasses. They look almost identical to ordinary glasses, but use specialized optics to signal the brain to slow the growth of myopic eyes.</p>
  </div>
  <div class="block photo-tag" style="left:40px;top:664px">Corvane.</div>

  <h3 class="block option-title" style="left:416px;top:350px">Low-dose Atropine</h3>
  <div class="block option-copy" style="left:416px;top:390px;width:330px">
    <p>These eyedrops have been studied for over 20 years and have been shown to slow myopia progression by about 50% when used consistently.</p>
    <p>Low-dose atropine is simple to add to your daily routine. One drop is placed in each eye before bed each evening. These are ordered from a compounding pharmacy and mailed directly to your home.</p>
  </div>

  <h3 class="block option-title" style="left:793px;top:350px">Specialty<br>Contact Lenses</h3>
  <div class="block option-copy" style="left:793px;top:418px;width:330px;line-height:26px">
    <p>FDA-approved ClearPath lenses have been shown to slow myopia progression by about 50% in children aged 8-12.</p>
    <p style="margin-top:26px">Contact lenses can be a great fit for many children, especially active children or those who do not enjoy wearing glasses. Many children as young as 7 or 8 are successful at wearing contacts.</p>
  </div>
</section>

</body>
</html>
```